Design AND code an HTML landing page

A landing page for campaigns and webinars respondents for project www.brevoa-homes.com. We expect the design to be coded. We will provide the copy and content. It will be a simple landing page for a new development project, to capture details of any potential clients showing interest, including any leads generated via webinars.

Broad instructions are as follows:
- It should not have a header or footer. Minimum escape links as possible.
- Create a lead generator box to get e-mails / relevant info of people interested.
- If possible, add a virtual tour (link to host server provided) at the top of the page.
- Content will be provided
- An option to include a link to a ClipHarbor video

Target Market(s)

Pre/retiree and retirees

Industry/Entity Type

Real estate development, retirement, relocation, travel and tourism

Coding

Coded - Design and coding required

Font styles to use
Other font styles liked:
• Preferably same as existing site

Colors
FFF300
FFF600
FEFA6F
FFFEC7
FFFEE8

Requirements
Must have
• Simple yet appealing look and feel, within the motif of the project, simple list of questions
Should not have
• Emojis, unrelated graphics, excessive graphics that are not linked to project

```html
<!DOCTYPE html>
<html lang="en">
<head>
<meta charset="utf-8">
<title>Brevoa Homes – Discover Most Suitable Property</title>
<link rel="stylesheet" href="https://fonts.googleapis.com/css2?family=Poppins:wght@300;400;500;600;700&display=swap">
<style>
:root{
  --yellow:#f2c40f;
  --yellow-soft:#fef3b8;
  --ink:#1f1f24;
  --muted:#6b6b72;
  --line:#e3e3e6;
  --grey-bg:#f4f4f5;
  --white:#ffffff;
}
*{box-sizing:border-box;margin:0;padding:0}
html,body{width:1200px;height:4360px;overflow:hidden}
body{font-family:"Poppins",sans-serif;color:var(--ink);background:var(--white);position:relative}
.abs{position:absolute}

/* Hero */
.hero{left:0;top:0;width:1200px;height:690px;overflow:hidden}
.hero-photo{position:absolute;inset:0;background:linear-gradient(180deg,#8fb3d6 0%,#b9cde0 30%,#6f8f6a 55%,#4d5f3e 75%,#8a7f70 100%)}
.hero-shade{position:absolute;right:0;top:0;width:600px;height:690px;background:linear-gradient(90deg,rgba(20,25,35,0) 0%,rgba(20,25,35,.45) 40%,rgba(20,25,35,.55) 100%)}
.brand{left:388px;top:36px;display:flex;align-items:center;gap:10px}
.brand-dot{width:52px;height:52px;border-radius:50%;background:var(--yellow)}
.brand-name{font-weight:600;font-size:22px;color:var(--white)}
.tour-btn{left:656px;top:44px;width:172px;height:40px;border-radius:20px;background:#1c1f27;color:var(--white);font-size:14px;display:flex;align-items:center;justify-content:center;gap:10px}
.hero-title{left:668px;top:232px;color:var(--white);font-size:58px;font-weight:700;line-height:1.02}
.hero-sub{left:668px;top:452px;width:320px;color:var(--white);font-size:14px;line-height:1.6;opacity:.92}
.hero-notch{left:578px;top:668px;width:44px;height:44px;border-radius:50%;background:var(--white);display:flex;align-items:center;justify-content:center}

/* About */
.about-title{left:128px;top:816px;font-size:34px;font-weight:700}
.about-title span,.accent{color:var(--yellow)}
.about-rule{left:128px;top:868px;width:52px;height:4px;background:var(--yellow)}
.about-text{left:128px;top:900px;width:380px;font-size:14px;line-height:1.85;color:var(--muted)}
.about-photo-main{left:600px;top:780px;width:260px;height:348px;background:linear-gradient(160deg,#c9d4dc,#5b6a55 55%,#2e3a2c);box-shadow:0 18px 40px rgba(0,0,0,.22)}
.about-photo-side{left:876px;top:822px;width:184px;height:264px;background:linear-gradient(160deg,#d7dde2,#7b8570 55%,#3a4235);box-shadow:0 14px 30px rgba(0,0,0,.18)}

/* Video band */
.band{left:0;top:1232px;width:1200px;height:540px;background:var(--yellow)}
.band-title{left:0;top:1280px;width:1200px;text-align:center;color:var(--white);font-size:28px;font-weight:600}
.band-sub{left:0;top:1326px;width:1200px;text-align:center;color:var(--white);font-size:11px;opacity:.9}
.band-btn{left:535px;top:1356px;width:130px;height:32px;border-radius:16px;background:var(--white);color:var(--ink);font-size:11px;font-weight:500;display:flex;align-items:center;justify-content:center}
.band-wave{left:0;top:1700px;width:1200px;height:140px}
.video{left:252px;top:1420px;width:696px;height:388px;background:linear-gradient(170deg,#b6c7d2 0%,#7f9377 40%,#3e4a3a 75%,#5d6f7a 100%);box-shadow:0 20px 40px rgba(0,0,0,.2)}
.video-bar{position:absolute;left:0;bottom:0;width:100%;height:34px;background:rgba(10,12,16,.65);display:flex;align-items:center;gap:12px;padding:0 14px;color:var(--white);font-size:11px}
.video-track{flex:1;height:4px;background:rgba(255,255,255,.35);position:relative}
.video-track i{position:absolute;left:0;top:0;width:18%;height:4px;background:var(--yellow)}

/* Facilities */
.section-title{left:0;width:1200px;text-align:center;font-size:38px;font-weight:700}
.section-sub{left:0;width:1200px;text-align:center;font-size:14px;color:var(--muted)}
.fac-card{top:2012px;width:228px;height:228px;border-radius:6px}
.fac-1{left:236px;background:linear-gradient(165deg,#cfd9e0,#7d8c70 55%,#3d8fb0)}
.fac-2{left:486px;background:linear-gradient(175deg,#9cc1dc,#5c7d95 50%,#2a2f36);overflow:hidden}
.fac-3{left:736px;background:linear-gradient(165deg,#a9c7e4,#b58a62 50%,#6d7d4d)}
.fac-label{position:absolute;left:0;bottom:0;width:100%;height:76px;background:rgba(15,17,22,.72);color:var(--white);text-align:center;font-size:13px;padding-top:18px}
.fac-label small{display:block;font-size:10px;letter-spacing:6px;opacity:.8;margin-top:4px}
.arrow{top:2110px;width:32px;height:32px;border-radius:50%;background:var(--white);box-shadow:0 2px 8px rgba(0,0,0,.15);display:flex;align-items:center;justify-content:center}

/* Features */
.reason-title{left:0;top:2330px;width:1200px;text-align:center;font-size:34px;font-weight:700;line-height:1.25}
.reason-title small{display:block;font-size:27px}
.arc{left:0;top:2400px;width:1200px;height:600px}
.feature{width:160px;text-align:center;font-size:13px;font-weight:500}
.feature-icon{width:76px;height:76px;margin:0 auto 12px;border-radius:50%;background:var(--white);border:1px solid var(--line);box-shadow:0 4px 14px rgba(0,0,0,.06);display:flex;align-items:center;justify-content:center}
.hub{left:440px;top:2720px;width:320px;height:320px;border-radius:50%;background:radial-gradient(circle,#fff 38%,#fdf1e6 39%,#fff 50%,#fbeadb 51%,#fff 62%,#fdf3ea 63%,rgba(255,255,255,0) 72%)}
.hub-brand{left:520px;top:2856px;width:160px;display:flex;align-items:center;justify-content:center;gap:8px}
.hub-brand .brand-dot{width:40px;height:40px}
.hub-brand .brand-name{color:var(--ink);font-size:16px}

/* Lead form */
.lead{left:0;top:3100px;width:1200px;height:720px;background:var(--grey-bg)}
.lead-photo{left:240px;top:3192px;width:352px;height:328px;background:linear-gradient(150deg,#e8c95a,#b8913a 50%,#6e5a2d)}
.form-card{left:400px;top:3288px;width:580px;height:432px;background:var(--white);box-shadow:0 18px 50px rgba(0,0,0,.12);padding:40px 48px}
.form-title{font-size:26px;font-weight:300;letter-spacing:1px;margin-bottom:30px}
.form-title b{font-weight:600}
.form-grid{display:grid;grid-template-columns:1fr 1fr;column-gap:40px;row-gap:22px}
.field{border-bottom:1px solid var(--line);padding-bottom:8px}
.field.wide{grid-column:1/3}
.field label{display:block;font-size:9px;font-weight:600;letter-spacing:.5px;margin-bottom:6px}
.field span{font-size:11px;color:#a4a4aa}
.send{position:absolute;right:48px;bottom:34px;width:50px;height:50px;border-radius:50%;background:var(--yellow);display:flex;align-items:center;justify-content:center}
.lead-wave{left:0;top:3770px;width:1200px;height:150px}

/* Contact */
.contact-title{left:0;top:3990px;width:1200px;text-align:center;font-size:34px;font-weight:700}
.contact-sub{left:0;top:4042px;width:1200px;text-align:center;font-size:14px;color:var(--muted)}
.contact-col{top:4140px;width:600px;text-align:center}
.contact-col h3{font-size:19px;font-weight:600;margin:24px 0 6px}
.contact-col p{font-size:15px}
.divider{left:600px;top:4120px;width:1px;height:220px;background:var(--line)}
</style>
</head>
<body>

<section class="hero abs">
  <div class="hero-photo" role="img" aria-label="Terrace with flowering plants and loungers overlooking town rooftops and the sea"></div>
  <div class="hero-shade"></div>
</section>
<div class="brand abs"><div class="brand-dot"></div><div class="brand-name">Brevoa Homes</div></div>
<a class="tour-btn abs">Virtual Tour
  <svg width="10" height="12" viewBox="0 0 10 12"><path d="M0 0L10 6 0 12z" fill="#fff"/></svg></a>
<h1 class="hero-title abs">Discover<br>Most Suitable<br>Property</h1>
<p class="hero-sub abs">Helping you to get your perfect properties in the locality, with the fastest way.</p>
<div class="hero-notch abs"><svg width="12" height="8" viewBox="0 0 12 8"><path d="M1 1l5 5 5-5" stroke="#1f1f24" stroke-width="2" fill="none"/></svg></div>

<h2 class="about-title abs">About <span>Brevoa Homes</span></h2>
<div class="about-rule abs"></div>
<p class="about-text abs">Nestled in the lush jungle of Bali between Canggu and Ubud, our incredible property sits on 3.3 hectares of land with a large river that flows through. We host 10 rooms at present and soon to be 30 more, expanding our scenic space so we can co-create new ideas, projects and technology that enable a healthier lifestyle.</p>
<div class="about-photo-main abs" role="img" aria-label="Aerial view of the apartment building with landscaped grounds"></div>
<div class="about-photo-side abs" role="img" aria-label="Apartment building facade seen from the street"></div>

<div class="band abs"></div>
<svg class="band-wave abs" viewBox="0 0 1200 140" preserveAspectRatio="none"><path d="M0 70 C200 20 380 20 600 60 C820 100 1000 110 1200 40 L1200 140 L0 140Z" fill="#fff"/><path d="M0 90 C220 40 400 50 600 80 C820 112 1000 120 1200 70" stroke="#f7dc6a" stroke-width="2" fill="none"/></svg>
<h2 class="band-title abs">Lorem ipsum dolor sit amet, consectetur</h2>
<p class="band-sub abs">Sed do eiusmod tempor incididunt ut labore et dolore</p>
<a class="band-btn abs">Learn more</a>
<div class="video abs" role="img" aria-label="Video still of the development with pool and gardens, hosted on ClipHarbor">
  <div class="video-bar">
    <svg width="10" height="12" viewBox="0 0 10 12"><path d="M0 0L10 6 0 12z" fill="#fff"/></svg>
    <span>0:42</span><div class="video-track"><i></i></div><span>3:15</span>
  </div>
</div>

<h2 class="section-title abs" style="top:1888px">The <span class="accent">Facilities</span></h2>
<p class="section-sub abs" style="top:1946px">Lorem ipsum dolor sit amet, consectetur adipiscing elit. Nulla laoreet eros</p>
<div class="arrow abs" style="left:112px"><svg width="8" height="12" viewBox="0 0 8 12"><path d="M7 1L2 6l5 5" stroke="#555" stroke-width="2" fill="none"/></svg></div>
<div class="fac-card fac-1 abs" role="img" aria-label="Pool area beside the apartment blocks"></div>
<div class="fac-card fac-2 abs" role="img" aria-label="Sea view from a furnished balcony">
  <div class="fac-label">Facilities<small>◦ ◦</small></div>
</div>
<div class="fac-card fac-3 abs" role="img" aria-label="Apartment building with lawn at sunset"></div>
<div class="arrow abs" style="left:1056px"><svg width="8" height="12" viewBox="0 0 8 12"><path d="M1 1l5 5-5 5" stroke="#555" stroke-width="2" fill="none"/></svg></div>

<h2 class="reason-title abs">Its the worlds #1<small>Destination <span class="accent">for a reason</span></small></h2>
<svg class="arc abs" viewBox="0 0 1200 600"><path d="M240 480 A360 360 0 0 1 960 480" stroke="#f0dcc8" stroke-width="2" fill="none"/></svg>
<div class="hub abs"></div>
<div class="hub-brand abs"><div class="brand-dot"></div><div class="brand-name">Brevoa Homes</div></div>

<div class="feature abs" style="left:520px;top:2474px"><div class="feature-icon"><svg width="30" height="30" viewBox="0 0 30 30"><circle cx="15" cy="15" r="8" fill="none" stroke="#1f1f24" stroke-width="2"/><path d="M4 5v20M26 5v20" stroke="#1f1f24" stroke-width="2"/></svg></div>The Feature</div>
<div class="feature abs" style="left:232px;top:2602px"><div class="feature-icon"><svg width="30" height="30" viewBox="0 0 30 30"><path d="M15 26C6 19 4 14 6 10c2-4 7-4 9 0 2-4 7-4 9 0 2 4 0 9-9 16z" fill="#1f1f24"/></svg></div>The Feature</div>
<div class="feature abs" style="left:808px;top:2602px"><div class="feature-icon"><svg width="30" height="30" viewBox="0 0 30 30"><path d="M5 25C5 12 13 5 26 5 26 18 18 25 5 25z" fill="#1f1f24"/><path d="M5 25L18 12" stroke="#fff" stroke-width="1.5"/></svg></div>The Feature</div>
<div class="feature abs" style="left:160px;top:2834px"><div class="feature-icon"><svg width="30" height="30" viewBox="0 0 30 30"><circle cx="15" cy="15" r="9" fill="#1f1f24"/><circle cx="15" cy="15" r="3.5" fill="#fff"/><path d="M15 2v5M15 23v5M2 15h5M23 15h5M6 6l3.5 3.5M20.5 20.5L24 24M6 24l3.5-3.5M20.5 9.5L24 6" stroke="#1f1f24" stroke-width="3"/></svg></div>The Feature</div>
<div class="feature abs" style="left:880px;top:2834px"><div class="feature-icon"><svg width="30" height="30" viewBox="0 0 30 30"><circle cx="15" cy="6" r="3" fill="#1f1f24"/><path d="M15 10v9M9 13l6 2 6-2M15 19l-5 8M15 19l5 8" stroke="#1f1f24" stroke-width="2.5" fill="none"/></svg></div>The Feature</div>

<div class="lead abs"></div>
<div class="lead-photo abs" role="img" aria-label="Couple reviewing property plans together"></div>
<form class="form-card abs">
  <h2 class="form-title">GET IN <b>TOUCH</b></h2>
  <div class="form-grid">
    <div class="field"><label>FIRST NAME*</label><span>First Name</span></div>
    <div class="field"><label>LAST NAME*</label><span>Last Name</span></div>
    <div class="field"><label>EMAIL ADDRESS*</label><span>name@example.com</span></div>
    <div class="field"><label>PHONE*</label><span>Your number</span></div>
    <div class="field wide"><label>COMPANY NAME</label><span>Company Name</span></div>
    <div class="field wide"><label>MESSAGE</label><span>Tell us what you are looking for in a new home</span></div>
  </div>
  <div class="send"><svg width="20" height="20" viewBox="0 0 20 20"><path d="M2 10L18 2 14 18 10 11z" fill="#fff"/></svg></div>
</form>
<svg class="lead-wave abs" viewBox="0 0 1200 150" preserveAspectRatio="none"><path d="M0 60 C240 10 420 20 640 70 C860 120 1020 110 1200 60 L1200 150 L0 150Z" fill="#fbe9a0"/><path d="M0 90 C260 40 440 50 640 95 C860 140 1030 130 1200 90 L1200 150 L0 150Z" fill="#fff"/></svg>

<h2 class="contact-title abs">Contact Us</h2>
<p class="contact-sub abs">We are here to help You</p>
<div class="contact-col abs" style="left:0">
  <svg width="40" height="40" viewBox="0 0 40 40"><path d="M9 5l7 1 2 8-4 3c2 4 5 7 9 9l3-4 8 2 1 7c-1 3-3 4-6 4C18 35 5 22 5 11c0-3 1-5 4-6z" fill="none" stroke="#f2c40f" stroke-width="2"/></svg>
  <h3>Have questions? Call Us.</h3><p>+1 555 014 0199</p>
</div>
<div class="divider abs"></div>
<div class="contact-col abs" style="left:600px">
  <svg width="40" height="40" viewBox="0 0 40 40"><rect x="5" y="9" width="30" height="22" fill="none" stroke="#f2c40f" stroke-width="2"/><path d="M5 9l15 13 15-13" fill="none" stroke="#f2c40f" stroke-width="2"/></svg>
  <h3>Email Us</h3><p>hello@brevoa-homes.com</p>
</div>

</body>
</html>
```